Need to make a work slip for trucking company.

I need a form to fill out for my truck drivers to get signed on delivery. It is for a trucking company and this form will be for each machine equipment move. I have included my old sheet which I need Updated. Its going on a 9.5 inch by 8.5 inch sheet of paper. It should have room for the day, date, customer name, ordered by, P.O. Number, Project Number, Driver, Truck/Trailer, Tolls (needs more room then my old sheet need a few lines under each other for each toll during the machine move), Permits, some room for other information, Loads, Hours, and 2 lines for a Signature and Print Line.
Updates

Need to also include a Pickup Address and a Deliver Address with lines to write in. Also I need to add a Print Line (and labeled Print) for whoever is signing the ticket.

Requirements
Must have
• My new company name and Logo. I have included my new Logo. It must be easy to ready. Must include my company colors. (Concrete Gray, and Neon Blue)

```html
<!DOCTYPE html>
<html lang="en">
<head>
<meta charset="utf-8">
<title>Ridgeway Haulage – Work Slip</title>
<link rel="stylesheet" href="https://fonts.googleapis.com/css2?family=Exo+2:wght@400;500;700&display=swap">
<style>
  :root {
    --backdrop: #b9def2;
    --paper: #ffffff;
    --panel: #fafafa;
    --brand-blue: #1a6bb5;
    --concrete: #8c8c8c;
    --ink: #1d1d1d;
    --chip: #e6e6e6;
    --rule: #b5b5b5;
    --deco-tone: #ececec;
  }
  * { box-sizing: border-box; margin: 0; padding: 0; }
  html, body { width: 1200px; height: 1200px; overflow: hidden; }
  body {
    background: var(--backdrop);
    font-family: "Exo 2", "Segoe UI", sans-serif;
    color: var(--ink);
    position: relative;
  }
  .sheet {
    position: absolute; left: 155px; top: 104px;
    width: 889px; height: 991px;
    background: var(--paper);
    overflow: hidden;
  }
  .abs { position: absolute; }
  .fill-panel { left: 0; top: 228px; width: 889px; height: 643px; background: var(--panel); }
  .corner-texture {
    left: 450px; top: 800px; width: 439px; height: 169px;
    background: linear-gradient(135deg, rgba(236,236,236,0) 30%, var(--deco-tone) 100%);
  }
  .side-tab { left: 857px; top: 40px; width: 32px; height: 117px; background: var(--brand-blue); }
  .footer-band { left: 0; top: 969px; width: 889px; height: 22px; background: var(--brand-blue); }

  .brand-name {
    left: 56px; top: 38px;
    font-size: 46px; font-weight: 700; line-height: 1.05;
    color: var(--brand-blue); letter-spacing: 0.5px;
  }

  .contact { right: 43px; top: 45px; text-align: right; color: var(--brand-blue); font-size: 18px; line-height: 28px; }
  .contact .company { font-size: 22px; font-weight: 700; line-height: 28px; }
  .contact .addr { margin-top: -4px; }

  .chip {
    position: absolute; height: 28px;
    background: var(--chip); border-radius: 4px;
    font-size: 18px; line-height: 29px; text-align: center;
  }
  .label { position: absolute; font-size: 17px; line-height: 20px; white-space: nowrap; }
  .rule { position: absolute; height: 0; border-top: 1px solid var(--rule); }
  .date-box { position: absolute; height: 28px; background: var(--chip); border-radius: 4px; }
</style>
</head>
<body>
<div class="sheet">
  <div class="abs fill-panel"></div>
  <div class="abs corner-texture" role="img" aria-label="Faint geometric line texture in the lower corner"></div>

  <div class="abs side-tab"></div>
  <div class="abs footer-band"></div>

  <div class="abs brand-name">RIDGEWAY<br>HAULAGE</div>

  <div class="abs contact">
    <div class="company">Ridgeway Haulage,</div>
    <div class="addr">Harbor Point, New York 11400</div>
    <div>Phone (555) 014 -3000</div>
    <div>Fax &nbsp;(555) 014 -3009</div>
  </div>

  <!-- day and time selectors -->
  <div class="chip" style="left:54px;top:189px;width:27px">M</div>
  <div class="chip" style="left:84px;top:189px;width:27px">T</div>
  <div class="chip" style="left:114px;top:189px;width:27px">W</div>
  <div class="chip" style="left:144px;top:189px;width:27px">T</div>
  <div class="chip" style="left:175px;top:189px;width:27px">F</div>
  <div class="chip" style="left:205px;top:189px;width:27px">S</div>
  <div class="chip" style="left:235px;top:189px;width:27px">S</div>
  <div class="chip" style="left:295px;top:189px;width:44px">A.M.</div>
  <div class="chip" style="left:343px;top:189px;width:44px">P.M.</div>

  <div class="label" style="left:497px;top:193px">Date:</div>
  <div class="date-box" style="left:545px;top:189px;width:291px"></div>

  <!-- job details -->
  <div class="label" style="left:55px;top:240px">Customer:</div>
  <div class="rule" style="left:143px;top:256px;width:697px"></div>
  <div class="label" style="left:55px;top:283px">Ordered By:</div>
  <div class="rule" style="left:156px;top:300px;width:684px"></div>
  <div class="label" style="left:55px;top:327px">P.O. No.:</div>
  <div class="rule" style="left:126px;top:343px;width:297px"></div>
  <div class="label" style="left:443px;top:328px">Project No.:</div>
  <div class="rule" style="left:544px;top:343px;width:296px"></div>

  <!-- equipment type selectors -->
  <div class="chip" style="left:126px;top:370px;width:45px">F/B</div>
  <div class="chip" style="left:177px;top:370px;width:45px">L/B</div>
  <div class="chip" style="left:228px;top:370px;width:44px">LD</div>
  <div class="chip" style="left:278px;top:370px;width:82px">STR/TRL</div>
  <div class="chip" style="left:365px;top:370px;width:74px">BM/TK</div>
  <div class="chip" style="left:445px;top:370px;width:92px">DUMP TK</div>
  <div class="chip" style="left:543px;top:370px;width:107px">ROLL BACK</div>
  <div class="chip" style="left:656px;top:370px;width:96px">ROLL OFF</div>

  <!-- left column -->
  <div class="label" style="left:54px;top:422px">Driver</div>
  <div class="rule" style="left:116px;top:440px;width:224px"></div>
  <div class="label" style="left:54px;top:460px">Tr. / Eq.</div>
  <div class="rule" style="left:123px;top:477px;width:217px"></div>
  <div class="label" style="left:54px;top:501px">L / W / H</div>
  <div class="rule" style="left:136px;top:516px;width:204px"></div>
  <div class="label" style="left:54px;top:541px">Tolls</div>
  <div class="rule" style="left:100px;top:556px;width:240px"></div>
  <div class="rule" style="left:100px;top:590px;width:240px"></div>
  <div class="rule" style="left:100px;top:624px;width:240px"></div>
  <div class="rule" style="left:100px;top:656px;width:240px"></div>
  <div class="rule" style="left:100px;top:687px;width:240px"></div>

  <div class="label" style="left:54px;top:720px">Permit(s)</div>
  <div class="rule" style="left:136px;top:739px;width:203px"></div>
  <div class="rule" style="left:54px;top:769px;width:286px"></div>
  <div class="label" style="left:54px;top:798px">Loads</div>
  <div class="rule" style="left:110px;top:814px;width:231px"></div>
  <div class="label" style="left:54px;top:832px">Hours</div>
  <div class="rule" style="left:110px;top:847px;width:230px"></div>

  <!-- right column -->
  <div class="label" style="left:472px;top:421px">Pickup Address</div>
  <div class="rule" style="left:601px;top:439px;width:239px"></div>
  <div class="rule" style="left:601px;top:470px;width:239px"></div>
  <div class="rule" style="left:601px;top:501px;width:239px"></div>
  <div class="rule" style="left:601px;top:533px;width:239px"></div>

  <div class="label" style="left:473px;top:573px">Deliver Address</div>
  <div class="rule" style="left:601px;top:588px;width:239px"></div>
  <div class="rule" style="left:601px;top:619px;width:239px"></div>
  <div class="rule" style="left:601px;top:651px;width:239px"></div>
  <div class="rule" style="left:601px;top:683px;width:239px"></div>

  <div class="label" style="left:472px;top:716px">Other</div>
  <div class="rule" style="left:528px;top:732px;width:312px"></div>
  <div class="rule" style="left:528px;top:765px;width:312px"></div>
  <div class="rule" style="left:528px;top:797px;width:312px"></div>
  <div class="rule" style="left:528px;top:831px;width:312px"></div>

  <!-- sign-off -->
  <div class="label" style="left:53px;top:883px">Signature</div>
  <div class="rule" style="left:129px;top:900px;width:711px"></div>
  <div class="label" style="left:53px;top:927px">Print</div>
  <div class="rule" style="left:100px;top:944px;width:740px"></div>
</div>
</body>
</html>
```